全国の1人〜2人で営業されている理・美容室のオーナーさん方にコロナでも全く影響を受けてない当サロンのノウハウを読んで頂きたいと思っています。
これからのサロンのあり方、考え方、今すぐに取り入れるべき技術や商品、売り上げの上げ方などをお伝えします。本気で環境を変えたい方、美容師の仕事、接客、人をキレイにすることが大好きな方、意識の高いお客様に囲まれずっと通って頂けるような、そんな美容室を一緒に作って行きたいです。

この度はご提案、修正と本当にありがとうございました。最後の最後までかなり悩みました。
初めての電子書籍で良い表紙デザインと出会うことが出来ました。

今回、ご提案頂いた皆さん、本当にありがとうございました。初心者の自分に親身になって頂き、皆さんの丁寧なデザインに感動しました。また2冊目も考えています。ご縁があればまたよろしくお願いします。

```html
<!DOCTYPE html>
<html lang="ja">
<head>
<meta charset="UTF-8">
<title>これからサロンが生き残る方法</title>
<link rel="stylesheet" href="https://fonts.googleapis.com/css2?family=Noto+Serif+JP:wght@900&family=Noto+Sans+JP:wght@700&display=swap">
<style>
  :root {
    --magenta: #e3177d;
    --paper: #ffffff;
    --ink: #1a1a1a;
    --figure-a: #f3dde6;
    --figure-b: #dfe9ef;
  }
  * { margin: 0; padding: 0; box-sizing: border-box; }
  html, body { width: 750px; height: 1200px; overflow: hidden; background: var(--paper); }
  .cover { position: relative; width: 750px; height: 1200px; overflow: hidden; background: var(--paper); }
  .cover__bands { position: absolute; inset: 0; }
  .figure {
    position: absolute;
    border-radius: 40px;
    background: linear-gradient(180deg, var(--figure-b) 0%, var(--figure-a) 45%, #f4f1ee 100%);
    opacity: 0.9;
  }
  .figure--hero { left: 225px; top: 640px; width: 300px; height: 560px; border-radius: 140px 140px 30px 30px; }
  .tagline {
    position: absolute; left: 612px; top: 30px;
    writing-mode: vertical-rl;
    font-family: "Noto Serif JP", serif; font-weight: 900;
    font-size: 64px; line-height: 1; letter-spacing: 2px;
    color: var(--ink);
    z-index: 2;
  }
  .title-box {
    position: absolute; left: 155px; top: 162px; width: 390px; height: 413px;
    background: var(--magenta);
    z-index: 2;
  }
  .title-box::after {
    content: ""; position: absolute; inset: 8px;
    border: 2px solid rgba(255,255,255,0.85);
  }
  .title {
    position: absolute; right: 22px; top: 38px;
    writing-mode: vertical-rl;
    font-family: "Noto Serif JP", serif; font-weight: 900;
    font-size: 80px; line-height: 88px;
    color: var(--paper);
  }
  .author {
    position: absolute; left: 155px; top: 582px; width: 390px; text-align: center;
    font-family: "Noto Sans JP", sans-serif; font-weight: 700;
    font-size: 34px; letter-spacing: 4px; color: var(--magenta);
    z-index: 2;
  }
</style>
</head>
<body>
<div class="cover">
  <svg class="cover__bands" width="750" height="1200" viewBox="0 0 750 1200" aria-hidden="true">
    <polygon points="0,612 325,1200 0,1200" fill="var(--magenta)"/>
    <polygon points="750,600 425,1200 750,1200" fill="var(--magenta)"/>
  </svg>

  <div class="figure" style="left:12px;top:10px;width:100px;height:230px" role="img" aria-label="Small illustration of a hairdresser with a raised finger"></div>
  <div class="figure" style="left:20px;top:255px;width:95px;height:190px" role="img" aria-label="Small illustration of a hairdresser giving an OK sign"></div>
  <div class="figure" style="left:55px;top:458px;width:85px;height:160px" role="img" aria-label="Small illustration of a puzzled hairdresser"></div>
  <div class="figure" style="left:30px;top:650px;width:90px;height:220px" role="img" aria-label="Small illustration of a hairdresser thinking"></div>
  <div class="figure" style="left:40px;top:930px;width:90px;height:250px" role="img" aria-label="Small illustration of a hairdresser pointing"></div>
  <div class="figure" style="left:550px;top:40px;width:56px;height:250px" role="img" aria-label="Small illustration of a hairdresser with crossed arms"></div>
  <div class="figure" style="left:550px;top:590px;width:56px;height:220px" role="img" aria-label="Small illustration of a hairdresser with a hand raised"></div>
  <div class="figure" style="left:610px;top:985px;width:90px;height:200px" role="img" aria-label="Small illustration of a hairdresser smiling"></div>
  <div class="figure figure--hero" role="img" aria-label="Illustration of a smiling hairdresser holding a brush and a hair dryer"></div>

  <p class="tagline">コロナや景気に左右されない</p>

  <div class="title-box">
    <h1 class="title">これから<br>サロンが<br>生き残る<br>方法</h1>
  </div>

  <p class="author">みずの はるか</p>
</div>
</body>
</html>
```